Stride42! Brochure

We need a bi-fold 8.5 inches by 11 inches standard size. The outline is attached with key sections included. The design needs to fit our brand standard and needs to be editable. We are requesting two rounds of edits. Photos can be provided to the selected designer to use. We are open to gatefold designs as well. The website for design reference is https://www.stride42.example/ . I will include the color palate and brochure content in the uploaded files.

```html
<!DOCTYPE html>
<html lang="en">
<head>
<meta charset="utf-8">
<title>Stride42! Brochure – Inside Spread</title>
<link rel="stylesheet" href="https://fonts.googleapis.com/css2?family=Michroma&family=Jura:wght@400;600&display=swap">
<style>
  :root {
    --backdrop: #e6e6e8;
    --paper: #f4f4f3;
    --orange: #ef6a3c;
    --mint: #8fd0bb;
    --navy: #0e2530;
    --ink: #4a4f55;
    --photo-warm: #b9a89a;
    --photo-cool: #4b5d9a;
  }
  * { margin: 0; padding: 0; box-sizing: border-box; }
  html, body { width: 1200px; height: 840px; overflow: hidden; background: var(--backdrop); }
  .spread {
    position: absolute; left: 60px; top: 70px;
    width: 1080px; height: 700px;
    display: flex;
    box-shadow: 0 18px 40px rgba(0,0,0,.18);
  }
  .page { position: relative; width: 540px; height: 700px; background: var(--paper); overflow: hidden; }
  .page--left { border-right: 1px solid #dcdcdc; }
  .page-art { position: absolute; inset: 0; }
  .heading {
    font-family: "Michroma", sans-serif; color: var(--orange);
    font-size: 24px; letter-spacing: .5px; line-height: 1.1; white-space: nowrap;
  }
  .subheading {
    font-family: "Michroma", sans-serif; color: var(--mint);
    font-size: 16px; line-height: 1.25; letter-spacing: .5px;
  }
  .body-copy {
    font-family: "Jura", sans-serif; color: var(--ink);
    font-size: 10.5px; line-height: 1.5; margin-top: 10px;
  }
  .body-copy + .body-copy { margin-top: 8px; }

  .text-column { position: absolute; left: 262px; top: 150px; width: 250px; }
  .text-column .heading + .body-copy { margin-top: 12px; }
  .who-we-are { margin-top: 38px; }

  .tagline {
    position: absolute; left: 28px; bottom: 56px; width: 190px;
    font-family: "Michroma", sans-serif; color: var(--mint);
    font-size: 13px; line-height: 1.35; letter-spacing: .5px;
  }

  .right-intro { position: absolute; left: 40px; top: 296px; width: 200px; }
  .what-we-do { position: absolute; left: 40px; top: 398px; width: 420px; }

  .services {
    position: absolute; left: 40px; top: 588px; width: 470px;
    display: grid; grid-template-columns: 1fr 1fr; gap: 16px 30px;
  }
  .service { display: flex; align-items: flex-start; gap: 10px; }
  .service-tag {
    flex: none; width: 56px; height: 22px; background: var(--mint);
    color: #fff; font-family: "Michroma", sans-serif; font-size: 9px;
    display: flex; align-items: center; justify-content: center; letter-spacing: .5px;
  }
  .service-text { font-family: "Jura", sans-serif; font-size: 10.5px; line-height: 1.35; color: var(--ink); }
</style>
</head>
<body>
<main class="spread">

  <section class="page page--left">
    <svg class="page-art" width="540" height="700" viewBox="0 0 540 700">
      <defs>
        <linearGradient id="studentPhotoTone" x1="0" y1="0" x2="1" y2="1">
          <stop offset="0" stop-color="#e9e4df"/>
          <stop offset=".55" stop-color="var(--photo-warm)"/>
          <stop offset="1" stop-color="#3a2e2a"/>
        </linearGradient>
      </defs>
      <polygon points="0,0 240,0 240,340 0,440" fill="url(#studentPhotoTone)" role="img" aria-label="Photo of a smiling student holding a phone"/>
      <polygon points="0,440 240,340 240,372 0,472" fill="var(--orange)"/>
      <polygon points="0,472 240,372 240,700 0,700" fill="var(--navy)"/>
      <rect x="262" y="40" width="14" height="40" fill="var(--orange)" transform="rotate(-18 269 60)"/>
      <line x1="300" y1="20" x2="330" y2="110" stroke="var(--mint)" stroke-width="3"/>
    </svg>

    <p class="tagline">DEVELOPING RELATIONSHIPS DELIVERING RESULTS...</p>

    <div class="text-column">
      <h2 class="heading">MISSION</h2>
      <p class="body-copy">Our mission at Stride42! is to increase the number of students who graduate from high school and college, and to help schools and counselors change lives one student at a time.</p>
      <p class="body-copy">We work as a true partner to districts, building counseling programs, supporting staff and measuring outcomes so every student leaves with a plan and a path.</p>

      <h2 class="heading who-we-are">WHO WE ARE</h2>
      <p class="body-copy">Stride42! was founded by former counselors and educators who saw how much a strong support system matters. Since then our team has partnered with schools across the country, helping thousands of students reach graduation and beyond.</p>
    </div>
  </section>

  <section class="page page--right">
    <svg class="page-art" width="540" height="700" viewBox="0 0 540 700">
      <defs>
        <linearGradient id="graduatesPhotoTone" x1="0" y1="0" x2="1" y2="1">
          <stop offset="0" stop-color="#d8d2cc"/>
          <stop offset=".5" stop-color="var(--photo-cool)"/>
          <stop offset="1" stop-color="#2c3566"/>
        </linearGradient>
      </defs>
      <polygon points="0,0 540,0 540,470 320,280 0,280" fill="url(#graduatesPhotoTone)" role="img" aria-label="Photo of smiling graduates in caps and gowns"/>
      <polygon points="320,280 480,418 468,432 308,294" fill="var(--orange)"/>
      <line x1="492" y1="434" x2="540" y2="476" stroke="var(--mint)" stroke-width="3"/>
    </svg>

    <h3 class="subheading right-intro">OUR PASSION IS TO HELP SCHOOLS AND STUDENTS</h3>

    <div class="what-we-do">
      <h2 class="heading">WHAT WE DO</h2>
      <p class="body-copy">Stride42! provides consulting, professional development, program design and performance management technology to ensure high schools and colleges achieve strong graduation rates and postsecondary success.</p>
      <p class="body-copy">Every school counselor and student we work with is evaluated based on their individual needs. Our comprehensive needs assessment helps us design a program around you and your students' needs.</p>
    </div>

    <div class="services">
      <div class="service"><span class="service-tag">HIRE</span><span class="service-text">We can help hire the right counseling staff for you</span></div>
      <div class="service"><span class="service-tag">COACH</span><span class="service-text">We can provide ongoing coaching for your staff</span></div>
      <div class="service"><span class="service-tag">TRAIN</span><span class="service-text">We can train your existing counseling staff</span></div>
      <div class="service"><span class="service-tag">TRACK</span><span class="service-text">We can track the results for your program including graduation rates, matriculation and persistence</span></div>
    </div>
  </section>

</main>
</body>
</html>
```